Industrial Company Profile Brochure Design

We need company profile brochure design. We are in industrial valve business and we are serving oil, petrochemical and power plants. We are working with our clients as trusted advisor. So, the final design should communicate valve solutions expert. The brochure should be 4 pages (including front and back) or folded style. However, it is open. We do not like to put any restriction on creativity. We leave the decision for number of pages and page size to the designer. The color theme should be same as / compatible with logo colors. You should use icons.Find attached the followings:- Our Logo- Word file that contains the required content (text and photos) for the brochure.3 Modern brochure designs. We like these designs. This is just to give you idea about what we like. The brochure is simple, clear and easy to get full information quickly.- Just banner for valve and components. You may need it.

Target Market(s)

The end users of oi, petrochemical and power plants

Industry/Entity Type

Engineering Consulting

Requirements
Must have
• - You must add our slogan. It is "Your Valves Solutions Expert"

```html
<!DOCTYPE html>
<html lang="en">
<head>
<meta charset="utf-8">
<title>Valteka Company Profile Brochure</title>
<link rel="stylesheet" href="https://fonts.googleapis.com/css2?family=Montserrat:wght@600;800&family=Open+Sans:wght@400;600;700&display=swap">
<style>
  :root {
    --orange: #f7941d;
    --grey: #8c8c8c;
    --grey-dark: #5a5a5a;
    --panel: #6d6d6d;
    --paper: #ffffff;
    --ink: #3d3d3d;
    --stage: #e4e4e4;
    --photo-a: #4d5d78;
    --photo-b: #9aa3b3;
  }
  * { margin: 0; padding: 0; box-sizing: border-box; }
  html, body { width: 855px; height: 1200px; overflow: hidden; }
  body { background: var(--stage); font-family: "Open Sans", sans-serif; color: var(--ink); position: relative; }

  .spread { position: absolute; left: 37px; width: 780px; height: 540px; background: var(--paper); box-shadow: 0 6px 18px rgba(0,0,0,.18); }
  .spread--outer { top: 40px; }
  .spread--inner { top: 620px; }
  .spread svg.art { position: absolute; inset: 0; width: 780px; height: 540px; }
  .fold { position: absolute; left: 389px; top: 0; width: 2px; height: 540px; background: rgba(0,0,0,.06); }

  .contact { position: absolute; left: 24px; top: 262px; font-size: 7px; line-height: 11px; color: var(--grey-dark); }
  .partners { position: absolute; left: 210px; top: 270px; display: flex; flex-direction: column; gap: 6px; }
  .partner-badge { width: 46px; height: 7px; border-radius: 4px; background: var(--grey); }
  .partner-badge--orange { background: var(--orange); }

  .cover-title { position: absolute; left: 420px; top: 360px; font-family: "Montserrat", sans-serif; font-weight: 800; font-size: 22px; line-height: 24px; color: var(--orange); letter-spacing: 1px; }
  .brand { position: absolute; left: 600px; top: 378px; display: flex; align-items: center; gap: 6px; }
  .brand-dot { width: 14px; height: 14px; border-radius: 50%; background: var(--orange); }
  .brand-name { font-family: "Montserrat", sans-serif; font-weight: 800; font-size: 20px; color: var(--orange); letter-spacing: 1px; }
  .slogan { position: absolute; left: 600px; top: 404px; font-size: 7.5px; font-weight: 600; color: var(--grey-dark); }

  .block { position: absolute; width: 150px; font-size: 6.5px; line-height: 9.5px; }
  .block h3 { font-family: "Montserrat", sans-serif; font-weight: 800; font-size: 8px; color: var(--orange); margin-bottom: 3px; letter-spacing: .5px; }
  .block p { color: var(--ink); }
  .block--about { left: 200px; top: 30px; }
  .block--mission { left: 200px; top: 110px; }
  .block--vision { left: 200px; top: 250px; }
  .block--why { left: 200px; top: 330px; }
  .block--products { left: 610px; top: 100px; }
  .block--services { left: 610px; top: 190px; }

  .panel { position: absolute; left: 410px; top: 290px; width: 170px; height: 220px; background: var(--panel); padding: 16px 14px; color: #fff; }
  .panel h3 { font-family: "Montserrat", sans-serif; font-weight: 800; font-size: 10px; line-height: 13px; margin-bottom: 8px; }
  .panel p { font-size: 7px; line-height: 10px; }
  .panel-tick { display: flex; gap: 5px; align-items: center; margin-top: 10px; }
</style>
</head>
<body>

<section class="spread spread--outer">
  <svg class="art" viewBox="0 0 780 540">
    <defs>
      <linearGradient id="plant" x1="0" y1="0" x2="1" y2="1">
        <stop offset="0" stop-color="var(--photo-b)"/><stop offset="1" stop-color="var(--photo-a)"/>
      </linearGradient>
    </defs>
    <polygon points="0,0 90,0 0,70" fill="var(--grey)"/>
    <polygon points="700,0 780,0 780,80" fill="var(--grey)"/>
    <polygon points="780,450 780,540 690,540" fill="var(--grey)"/>
    <polygon points="150,150 330,150 600,300 420,300" fill="var(--orange)"/>
    <g role="img" aria-label="Photo of industrial valve equipment in a workshop">
      <polygon points="205,20 300,75 300,185 205,240 110,185 110,75" fill="url(#plant)"/>
    </g>
    <g role="img" aria-label="Photo of valve testing rig in a plant">
      <polygon points="600,150 680,196 680,288 600,334 520,288 520,196" fill="url(#plant)"/>
    </g>
    <polygon points="470,300 496,315 496,345 470,360 444,345 444,315" fill="var(--grey)"/>
  </svg>
  <div class="fold"></div>
  <div class="contact">
    <p>P.O. Box 4120, Dammam 31452</p>
    <p>Tel: +966 13 555 0142</p>
    <p>info@valteka-valves.com</p>
    <p>www.valteka-valves.com</p>
  </div>
  <div class="partners">
    <span class="partner-badge"></span>
    <span class="partner-badge partner-badge--orange"></span>
    <span class="partner-badge"></span>
  </div>
  <h1 class="cover-title">COMPANY<br>PROFILE</h1>
  <div class="brand"><span class="brand-dot"></span><span class="brand-name">VALTEKA</span></div>
  <p class="slogan">Your Valves Solutions Expert</p>
</section>

<section class="spread spread--inner">
  <svg class="art" viewBox="0 0 780 540">
    <defs>
      <linearGradient id="plant2" x1="0" y1="0" x2="1" y2="1">
        <stop offset="0" stop-color="var(--photo-b)"/><stop offset="1" stop-color="var(--photo-a)"/>
      </linearGradient>
    </defs>
    <polygon points="0,420 0,540 70,540" fill="var(--grey)"/>
    <polygon points="110,130 165,130 60,540 0,540 0,500" fill="var(--orange)"/>
    <g role="img" aria-label="Photo of large industrial valve">
      <polygon points="80,10 145,48 145,122 80,160 15,122 15,48" fill="url(#plant2)"/>
    </g>
    <polygon points="700,0 780,0 780,80" fill="var(--orange)"/>
    <polygon points="780,460 780,540 700,540" fill="var(--grey)"/>
    <g role="img" aria-label="Product photos of valves and components">
      <rect x="420" y="40" width="50" height="40" rx="4" fill="var(--photo-b)"/>
      <rect x="480" y="40" width="50" height="40" rx="4" fill="var(--grey)"/>
      <rect x="540" y="40" width="50" height="40" rx="4" fill="var(--photo-a)"/>
      <rect x="420" y="90" width="170" height="60" rx="4" fill="#cfd3da"/>
    </g>
    <g role="img" aria-label="Photo of valve actuator">
      <polygon points="680,300 725,326 725,378 680,404 635,378 635,326" fill="url(#plant2)"/>
    </g>
  </svg>
  <div class="fold"></div>
  <div class="block block--about"><h3>ABOUT US</h3><p>Valteka supplies and services industrial valves for oil, petrochemical and power plants across the region.</p></div>
  <div class="block block--mission"><h3>OUR MISSION</h3><p>To keep every plant running safely with the right valve, delivered on time.</p></div>
  <div class="block block--vision"><h3>OUR VISION</h3><p>To be the trusted valve advisor for every process plant we serve.</p></div>
  <div class="block block--why"><h3>WHY CHOOSE US</h3><p>Certified engineers, fast response, genuine parts and full technical support from selection to start up.</p></div>
  <div class="block block--products"><h3>OUR PRODUCTS</h3><p>Gate, globe, ball, check and control valves with actuators and spare components.</p></div>
  <div class="block block--services"><h3>OUR SERVICES</h3><p>Inspection, repair, testing, overhaul and on-site valve maintenance.</p></div>
  <div class="panel">
    <h3>Serving Oil, Petrochemical &amp; Power Plants</h3>
    <p>Field crews available around the clock for shutdowns and emergencies.</p>
    <div class="panel-tick">
      <svg width="12" height="12" viewBox="0 0 12 12"><circle cx="6" cy="6" r="6" fill="var(--orange)"/><path d="M3 6.2l2 2 4-4.4" stroke="#fff" stroke-width="1.5" fill="none"/></svg>
      <svg width="12" height="12" viewBox="0 0 12 12"><circle cx="6" cy="6" r="6" fill="var(--orange)"/><path d="M3 6.2l2 2 4-4.4" stroke="#fff" stroke-width="1.5" fill="none"/></svg>
      <svg width="12" height="12" viewBox="0 0 12 12"><circle cx="6" cy="6" r="6" fill="var(--orange)"/><path d="M3 6.2l2 2 4-4.4" stroke="#fff" stroke-width="1.5" fill="none"/></svg>
    </div>
  </div>
</section>

</body>
</html>
```